Business Card Design

Contact Information for Business Card

A vertical business card request- a medium & light gray with silverfern tree logo (logo is attached)

Please use Trebuchet font -- if possible- can we use two different color gray? (See pictures attached below)
Info on the front should be the Silverfern tree logo - on the top of the card, followed by the info ...
Card to read: " " indicated what should be on the card --
Name: " Joan Pelley "
Title : "Partner "
" Office: 202.555.0147 "
" Mobile: 202.555.0182 "

Backside of the card - solid medium color gray color w/ address and small message centered in the card - Trebuchet font
to read:

" 317 B North Linden Avenue, NE "
" Washington, DC 20099 "

Then below address to read:
" Fundraising | Event Planning | Political Consulting "

```html
<!DOCTYPE html>
<html lang="en">
<head>
<meta charset="utf-8">
<title>Silverfern Strategies – Business Card</title>
<link href="https://fonts.googleapis.com/css2?family=Source+Sans+3:wght@400;600&display=swap" rel="stylesheet">
<style>
  :root {
    --backdrop-top: #2b2b2b;
    --backdrop-bottom: #000000;
    --card-grey: #5f6062;
    --mark-grey: #8a8b8d;
    --ink-white: #f2f2f2;
    --ink-soft: #e4e4e4;
  }
  * { margin: 0; padding: 0; box-sizing: border-box; }
  html, body { width: 1200px; height: 900px; overflow: hidden; }
  body {
    background: linear-gradient(to bottom, var(--backdrop-top), var(--backdrop-bottom) 85%);
    font-family: "Source Sans 3", "Trebuchet MS", sans-serif;
    position: relative;
  }
  .card {
    position: absolute;
    top: 184px;
    height: 490px;
    background: var(--card-grey);
    border-radius: 12px;
    color: var(--ink-white);
  }
  .card--front { left: 299px; width: 301px; }
  .card--back  { left: 645px; width: 305px; }

  .brand-dot {
    position: absolute;
    width: 120px;
    height: 120px;
    border-radius: 50%;
    background: var(--mark-grey);
  }
  .card--front .brand-dot { left: 118px; top: 88px; }
  .card--back .brand-dot  { left: 128px; top: 76px; }

  .wordmark {
    position: absolute;
    color: var(--ink-soft);
    font-weight: 400;
    text-transform: uppercase;
    text-align: right;
    line-height: 1;
  }
  .card--front .wordmark { left: 29px; width: 230px; top: 214px; }
  .card--back .wordmark  { left: 45px; width: 223px; top: 202px; }
  .wordmark__name { display: block; font-size: 27px; letter-spacing: 3px; margin-right: -3px; }
  .wordmark__line { display: block; font-size: 13px; letter-spacing: 1.2px; margin-top: 3px; margin-right: -1px; }

  .contact {
    position: absolute;
    left: 0; right: 0;
    top: 332px;
    text-align: center;
  }
  .contact__name { font-size: 19.5px; font-weight: 600; line-height: 22px; letter-spacing: 0.3px; }
  .contact__title { font-size: 15.5px; line-height: 20px; }
  .contact__phones { list-style: none; margin-top: 27px; font-size: 16px; line-height: 22px; }
  .contact__phones li { display: flex; justify-content: center; align-items: center; gap: 6px; }
  .contact__phones svg { width: 11px; height: 13px; fill: var(--ink-white); }

  .address {
    position: absolute;
    left: 0; right: 0;
    top: 311px;
    text-align: center;
    font-size: 16.5px;
    font-weight: 600;
    line-height: 22px;
  }
  .services {
    position: absolute;
    left: 0; right: 0;
    top: 367px;
    list-style: none;
    text-align: center;
    font-size: 17px;
    line-height: 29.5px;
  }
  .services li::before {
    content: "";
    display: inline-block;
    width: 8px; height: 8px;
    border-radius: 50%;
    background: var(--ink-white);
    margin-right: 5px;
    vertical-align: 2px;
  }
</style>
</head>
<body>
  <section class="card card--front" aria-label="Card front">
    <div class="brand-dot" role="img" aria-label="Silverfern logo mark area"></div>
    <div class="wordmark">
      <span class="wordmark__name">Silverfern</span>
      <span class="wordmark__line">Strategies</span>
    </div>
    <div class="contact">
      <p class="contact__name">JOAN PELLEY</p>
      <p class="contact__title">Partner</p>
      <ul class="contact__phones">
        <li>
          <svg viewBox="0 0 12 12" aria-label="Office"><path d="M2.6 0.5l2 2.4-1.1 1.5c0.7 1.6 2 2.9 3.6 3.6l1.5-1.1 2.4 2-1 2.3C5 11 1 7 0.3 1.5z"/></svg>
          <span>202.555.0147</span>
        </li>
        <li>
          <svg viewBox="0 0 8 13" aria-label="Mobile"><path d="M1.5 0h5a1.5 1.5 0 0 1 1.5 1.5v10A1.5 1.5 0 0 1 6.5 13h-5A1.5 1.5 0 0 1 0 11.5v-10A1.5 1.5 0 0 1 1.5 0zM1.4 1.6v8.4h5.2V1.6zM4 10.6a0.8 0.8 0 1 0 0 1.6a0.8 0.8 0 0 0 0-1.6z"/></svg>
          <span>202.555.0182</span>
        </li>
      </ul>
    </div>
  </section>

  <section class="card card--back" aria-label="Card back">
    <div class="brand-dot" role="img" aria-label="Silverfern logo mark area"></div>
    <div class="wordmark">
      <span class="wordmark__name">Silverfern</span>
      <span class="wordmark__line">Strategies</span>
    </div>
    <p class="address">317 B North Linden Avenue, NE<br>Washington, DC 20099</p>
    <ul class="services">
      <li>Fundraising</li>
      <li>Event Planning</li>
      <li>Political Consulting</li>
    </ul>
  </section>
</body>
</html>
```